Country House in Italy Needs a Business Card Design

We need a business card design for “Casale del Ruscello”, a modern concept of a Farm Holidays/Country House to be opened in central Italy.
Attached is the company logo you did for us in the past.
Please
- create a double-sided business card design
- on the back I would like to have the logo
- on the front the copy
Copy on card:
o Casale del Ruscello
o Address: Via Fontalba, 14
Cingoli (MC), Italy
o Website: www.casaledelruscello.it
o Email: info@casaledelruscello.it
o my name : Lucilla
o my mobile phone number: +39 347 8124591
In the distribution of information keep in mind the possible inclusion also of a landline telephone number (currently not available / existing).
WE WOULD LIKE TO HAVE A MODERN, PROFFESIONAL, OUT OF THE BOX BUSINESS CARD. BE AS CREATIVE AS YOU WOULD LIKE.

```html
<!DOCTYPE html>
<html lang="en">
<head>
<meta charset="utf-8">
<title>Casale del Ruscello – Business Card, Back and Front</title>
<link rel="stylesheet" href="https://fonts.googleapis.com/css2?family=Open+Sans:wght@400;600;700&display=swap">
<style>
  :root {
    --page-bg: #ecebe8;
    --card-white: #ffffff;
    --card-shade: #e9e9e9;
    --tan-light: #e6c590;
    --tan-dark: #c9a06b;
    --accent-orange: #f07a3c;
    --ink-dark: #3a3a3a;
    --ink-brown: #4a3826;
    --logo-brown: #8a6a4c;
  }
  * { margin: 0; padding: 0; box-sizing: border-box; }
  html, body {
    width: 1200px; height: 900px; overflow: hidden;
    background: var(--page-bg);
    font-family: "Open Sans", Arial, sans-serif;
  }
  .card {
    position: absolute;
    width: 900px; height: 514px;
    border-radius: 48px;
    overflow: hidden;
    background: linear-gradient(160deg, var(--card-white) 40%, var(--card-shade) 100%);
    box-shadow: 0 18px 40px rgba(0,0,0,0.18);
    transform-origin: top left;
    transform: scale(0.78);
  }
  .card-back { left: 249px; top: 38px; }
  .card-front { left: 249px; top: 460px; }
  .card-shapes { position: absolute; inset: 0; width: 100%; height: 100%; }

  .brand { position: absolute; display: flex; align-items: center; gap: 18px; }
  .brand-dot { border-radius: 50%; background: var(--tan-dark); flex: none; }
  .brand-name { font-weight: 400; color: var(--logo-brown); letter-spacing: 0.5px; white-space: nowrap; }

  .card-back .brand {
    left: 0; right: 0; top: 0; bottom: 0;
    justify-content: center; gap: 26px;
  }
  .card-back .brand-dot { width: 110px; height: 110px; }
  .card-back .brand-name { font-size: 48px; }

  .card-front .brand { left: 250px; top: 96px; }
  .card-front .brand-dot { width: 74px; height: 74px; }
  .card-front .brand-name { font-size: 34px; }

  .holder { position: absolute; right: 290px; top: 176px; text-align: right; white-space: nowrap; }
  .holder-name { font-size: 25px; font-weight: 700; color: var(--ink-dark); }
  .holder-role { font-size: 22px; font-weight: 400; color: var(--ink-dark); margin-top: 2px; }

  .contact {
    position: absolute; left: 70px; top: 356px;
    font-size: 17px; line-height: 1.35; color: var(--ink-brown);
    list-style: none;
  }
  .contact .gap { margin-top: 12px; }
</style>
</head>
<body>
  <div class="card card-back">
    <div class="brand">
      <span class="brand-dot"></span>
      <span class="brand-name">Casale del Ruscello</span>
    </div>
  </div>

  <div class="card card-front">
    <svg class="card-shapes" viewBox="0 0 900 514" preserveAspectRatio="none" aria-hidden="true">
      <defs>
        <linearGradient id="tanBand" x1="0" y1="1" x2="1" y2="0">
          <stop offset="0" stop-color="var(--tan-light)"/>
          <stop offset="1" stop-color="var(--tan-dark)"/>
        </linearGradient>
      </defs>
      <path class="tan-band" fill="url(#tanBand)"
            d="M0,282 C230,318 470,330 640,272 C770,228 860,120 830,0 L900,0 L900,514 L0,514 Z"/>
      <path class="white-rule" fill="#ffffff"
            d="M0,276 C230,312 470,322 636,262 C762,216 846,112 812,0 L830,0 C860,120 770,228 640,272 C470,330 230,318 0,282 Z"/>
      <path class="orange-swoosh" fill="var(--accent-orange)"
            d="M120,288 C300,314 480,312 630,252 C752,204 826,104 784,0 L808,0 C842,110 760,212 634,260 C480,318 300,316 120,288 Z"/>
    </svg>

    <div class="brand">
      <span class="brand-dot"></span>
      <span class="brand-name">Casale del Ruscello</span>
    </div>

    <div class="holder">
      <p class="holder-name">Marlo Fenwick-Hale</p>
      <p class="holder-role">Consultant</p>
    </div>

    <ul class="contact">
      <li>P : +39 347 8124591</li>
      <li>F : +39 0733 604218</li>
      <li class="gap">marlo@casaledelruscello.it</li>
      <li>www.casaledelruscello.it</li>
      <li>Via Fontalba, 14 · Cingoli (MC), Italy</li>
    </ul>
  </div>
</body>
</html>
```